2 page flyer outlining details of a product framework

We need a flyer for a management consulting firm outlining a product we offer. The draft wording and company logo are attached. Logo colours should be used (Purple - C73, M93, Y0, K0 & Green - C50, M0, Y99, K0).
The look and feel should communicate a dynamic, trustworthy, credible organisation with excellence in delivery.

File must be provided in AI format to enable text changes.

Target Market(s)

Senior Business Excecutives

Industry/Entity Type

Management Consulting

Font styles to use
Other font styles liked:
• Aller & Myriad Pro

Colors
acd036
6b449b

Requirements
Must have
• Logo & wording provided, professional images and a flyer layout with space and a section for contact details.

```html
<!DOCTYPE html>
<html lang="en">
<head>
<meta charset="utf-8">
<title>Peak Aligned Workforce Framework Assessment – Flyer</title>
<link rel="stylesheet" href="https://fonts.googleapis.com/css2?family=Lato:wght@400;700;900&family=Roboto+Condensed:wght@700&family=Ubuntu:wght@500;700&family=Anton&display=swap">
<style>
  :root {
    --purple: #6b449b;
    --purple-deep: #4f2a7f;
    --green: #acd036;
    --green-deep: #7fae1f;
    --ink: #3a3a3a;
    --ink-soft: #555;
    --paper: #f4f4f4;
    --white: #ffffff;
    --photo-dark: #1b2c4a;
    --photo-light: #5d8cc4;
  }
  * { margin: 0; padding: 0; box-sizing: border-box; }
  html, body { width: 920px; height: 1200px; overflow: hidden; background: var(--white); }
  .flyer { position: relative; width: 920px; height: 1200px; overflow: hidden; background: var(--paper); font-family: "Lato", sans-serif; color: var(--ink); }

  .green-column { position: absolute; left: 0; top: 100px; width: 460px; height: 1060px;
    background: linear-gradient(160deg, #bfe04a 0%, var(--green) 45%, var(--green-deep) 100%); }
  .info-column { position: absolute; left: 460px; top: 300px; width: 460px; height: 860px;
    background: linear-gradient(180deg, #fafafa 0%, #e8e8e8 100%); }

  .hero { position: absolute; left: 0; top: 0; width: 920px; height: 470px; }

  .pillars { position: absolute; left: 0; top: 440px; width: 460px; padding: 0 22px 0 26px; }
  .pillar { margin-bottom: 16px; }
  .pillar-head { display: flex; align-items: flex-start; gap: 14px; margin-bottom: 12px; }
  .pillar-number { font-family: "Anton", sans-serif; font-size: 68px; line-height: 62px; color: var(--white);
    width: 54px; text-align: center; flex: none; }
  .pillar-title { font-weight: 900; font-size: 16px; line-height: 1.25; color: var(--white); padding-top: 4px; }
  .pillar-intro { font-weight: 700; font-size: 13.5px; line-height: 1.35; color: #2e3a12; margin-bottom: 5px; }
  .pillar-list { list-style: none; }
  .pillar-list li { position: relative; padding-left: 18px; font-weight: 700; font-size: 13px; line-height: 1.35;
    color: #33401a; margin-bottom: 4px; }
  .pillar-list li::before { content: ""; position: absolute; left: 2px; top: 5px; width: 8px; height: 8px;
    border-radius: 50%; background: var(--white); }

  .title-box { position: absolute; left: 460px; top: 470px; width: 460px; height: 118px; background: var(--white);
    text-align: center; padding-top: 18px; }
  .product-name { font-family: "Ubuntu", sans-serif; font-weight: 700; font-size: 50px; line-height: 1; color: var(--purple); }
  .product-sub { font-weight: 700; font-size: 19px; color: #444; margin-top: 8px; }
  .product-sub em { font-style: normal; color: var(--green-deep); }

  .question-band { position: absolute; left: 460px; top: 588px; width: 460px; height: 128px;
    background: linear-gradient(180deg, #7a52ab, var(--purple-deep)); padding: 18px 20px 0 30px;
    font-family: "Roboto Condensed", sans-serif; font-size: 23px; line-height: 1.3; }
  .question-band .ask { color: var(--white); }
  .question-band .challenge { color: var(--green); }

  .pitch { position: absolute; left: 460px; top: 745px; width: 460px; padding: 0 30px; }
  .pitch-headline { font-weight: 700; font-size: 24px; line-height: 1.3; color: #4a4a4a; }
  .pitch-headline .big { font-size: 27px; }
  .pitch-body { margin-top: 22px; font-weight: 700; font-size: 15.5px; line-height: 1.4; color: var(--ink-soft); text-align: justify; }

  .footer-curve { position: absolute; left: 0; top: 940px; width: 920px; height: 260px; }

  .brand-badge { position: absolute; left: 585px; top: 1012px; width: 170px; height: 170px; border-radius: 50%;
    background: var(--white); display: flex; flex-direction: column; align-items: center; justify-content: center; text-align: center; }
  .brand-name { font-family: "Lato", sans-serif; font-weight: 900; font-size: 24px; line-height: 1.1; color: var(--purple); }
</style>
</head>
<body>
<main class="flyer">
  <div class="green-column"></div>
  <div class="info-column"></div>

  <svg class="hero" viewBox="0 0 920 470" aria-hidden="false">
    <defs>
      <linearGradient id="photoTone" x1="0" y1="0" x2="1" y2="1">
        <stop offset="0" stop-color="#3f6ea8"/>
        <stop offset="0.45" stop-color="#27456e"/>
        <stop offset="1" stop-color="#1b2c4a"/>
      </linearGradient>
      <linearGradient id="swoosh" x1="0" y1="0" x2="1" y2="0">
        <stop offset="0" stop-color="#7e56b0"/>
        <stop offset="1" stop-color="#4f2a7f"/>
      </linearGradient>
    </defs>
    <path role="img" aria-label="Photo: a businessman's hand touching a glowing network of connected people icons"
          d="M0,0 H920 V440 C650,420 310,330 0,120 Z" fill="url(#photoTone)"/>
    <path d="M0,120 C310,330 650,420 920,440 L920,470 C630,460 290,400 0,210 Z" fill="url(#swoosh)"/>
  </svg>

  <section class="pillars">
    <article class="pillar">
      <div class="pillar-head"><span class="pillar-number">1</span>
        <h3 class="pillar-title">Planning Capability – how well do you predict and plan for the future?</h3></div>
      <p class="pillar-intro">We review how you approach forecasting and scheduling activities, including;</p>
      <ul class="pillar-list">
        <li>Data accuracy and validity</li>
        <li>Known variations (i.e. Public Holidays &amp; Marketing activities)</li>
        <li>Assumptions used in the planning process</li>
      </ul>
    </article>
    <article class="pillar">
      <div class="pillar-head"><span class="pillar-number">2</span>
        <h3 class="pillar-title">Real Time Management – how well do you respond to changing needs and unexpected events?</h3></div>
      <p class="pillar-intro">We review how you manage intraday activities, including;</p>
      <ul class="pillar-list">
        <li>Reforecasting and planning</li>
        <li>Managing exceptions</li>
        <li>Recovery strategies</li>
      </ul>
    </article>
    <article class="pillar">
      <div class="pillar-head"><span class="pillar-number">3</span>
        <h3 class="pillar-title">System Interaction and Acceptance – how well have you enabled and empowered your team to get the most out of the system?</h3></div>
      <p class="pillar-intro">We review how you utilise and enable capabilities such as;</p>
      <ul class="pillar-list">
        <li>Use of self-service functionality</li>
        <li>Use of meeting and training scheduling functionality</li>
        <li>Support team autonomy and interaction with the system</li>
      </ul>
    </article>
    <article class="pillar">
      <div class="pillar-head"><span class="pillar-number">4</span>
        <h3 class="pillar-title">Reporting – how well are you using the valuable data available to make informed business decisions?</h3></div>
      <p class="pillar-intro">We review how you utilise available reports and data,</p>
      <ul class="pillar-list">
        <li>Information currently reported</li>
        <li>Inclusion of workforce management metrics in management reports</li>
        <li>Accuracy and validity of reported metrics</li>
      </ul>
    </article>
  </section>

  <header class="title-box">
    <h1 class="product-name">Peak Aligned</h1>
    <p class="product-sub">Workforce <em>(PAW!)</em> Framework Assessment</p>
  </header>

  <section class="question-band">
    <p class="ask">How much is inefficient workforce management costing your business?</p>
    <p class="challenge">Are you as efficient as you could be?</p>
  </section>

  <section class="pitch">
    <h2 class="pitch-headline">Find the answers with a powerful <span class="big">Peak Aligned Workforce ™</span> (PAW!) Framework Assessment!</h2>
    <p class="pitch-body">We provide a detailed, tailored assessment based on our proprietary PAW! Framework. Our framework is scalable and flexible to suit organisations of any size and structure – providing you with a roadmap to successfully achieving better business outcomes, greater efficiency, and cost savings.</p>
  </section>

  <svg class="footer-curve" viewBox="0 0 920 260" aria-hidden="true">
    <path d="M920,20 C860,150 700,200 460,210 L0,218 V260 H920 Z" fill="#6b449b"/>
    <path d="M920,20 C880,120 760,175 600,196 C760,165 870,110 920,60 Z" fill="#4f2a7f"/>
    <path d="M0,232 L460,226 C620,222 760,212 920,196 V202 C760,218 620,228 460,232 L0,238 Z" fill="#ffffff"/>
  </svg>

  <div class="brand-badge">
    <p class="brand-name">KESTREL<br>Management<br>Consulting</p>
  </div>
</main>
</body>
</html>
```